Esthetically Pleasing Core Values and Brand Promise for Accounting Firm

I would like a cohesive design that ties together my core values and brand promise. My firm, Maple Finch Advisory, provides accounting work to small businesses. I prefer modern and clean designs. I want my Core Values and Brand Promise to represent me - sole entrepreneur, married, mother of two kids, modern esthetics, clean lines, organized, colorful (teals, greys, white, yellows)

Industry/Entity Type

Public Accounting

Colors
33b8a4

```html
<!DOCTYPE html>
<html lang="en">
<head>
<meta charset="UTF-8">
<title>Maple Finch Advisory – Core Values &amp; Brand Promise</title>
<link href="https://fonts.googleapis.com/css2?family=Montserrat:wght@400;500;600;700;800&display=swap" rel="stylesheet">
<style>
  :root {
    --teal: #33b8a4;
    --yellow: #fbc82f;
    --charcoal: #474747;
    --crimson: #e23957;
    --ink: #151515;
    --white: #ffffff;
    --paper-bg: #ffffff;
    --shadow: rgba(0,0,0,0.16);
  }
  * { box-sizing: border-box; margin: 0; padding: 0; }
  html, body {
    width: 1200px; height: 1200px; overflow: hidden;
    background: var(--paper-bg);
    font-family: "Montserrat", sans-serif;
  }
  .sheet {
    position: absolute;
    left: 190px; top: 20px;
    width: 1052px; height: 1488px;
    transform: scale(0.78);
    transform-origin: 0 0;
    background: var(--white);
  }
  .values-panel {
    position: absolute; left: 58px; top: 56px;
    width: 928px; height: 846px;
    background: var(--teal);
  }
  .values-heading {
    position: absolute;
    left: 36px; top: 812px;
    transform: rotate(-90deg);
    transform-origin: 0 0;
    font-size: 116px; font-weight: 800;
    letter-spacing: 1px; line-height: 1;
    white-space: nowrap;
    color: var(--white);
  }
  .values-heading .dark { color: var(--ink); }

  .value {
    position: absolute; left: 224px;
    width: 640px; height: 148px;
  }
  .value__halo {
    position: absolute; left: 18px; top: 0;
    width: 460px; height: 148px;
    background: var(--white);
    border-radius: 74px;
  }
  .value__bar {
    position: absolute; left: 43px; top: 14px;
    width: 585px; height: 120px;
    border-radius: 60px;
    box-shadow: 6px 8px 12px var(--shadow);
    padding: 20px 40px 0 75px;
    color: var(--white);
  }
  .value__icon {
    position: absolute; left: 0; top: 24px;
    width: 66px; height: 96px;
    background: var(--white);
    border-radius: 10px;
    display: flex; align-items: center; justify-content: center;
    box-shadow: 2px 3px 6px var(--shadow);
  }
  .value__title { font-size: 25px; font-weight: 700; letter-spacing: 0.5px; margin-bottom: 4px; }
  .value__text { font-size: 16.5px; font-weight: 400; line-height: 1.08; letter-spacing: 0.3px; }
  .value--empower .value__bar { background: var(--teal); }
  .value--client .value__bar { background: var(--yellow); }
  .value--rectitude .value__bar { background: var(--charcoal); }
  .value--relentless .value__bar { background: var(--crimson); }

  .brand-promise {
    position: absolute; left: 77px; top: 950px; width: 720px;
    font-size: 24.5px; font-weight: 700; letter-spacing: 0.5px; line-height: 1.3;
    color: var(--ink);
  }
  .brand-promise .accent { color: var(--teal); }

  .service {
    position: absolute; top: 1055px;
    width: 307px; height: 250px;
    background: var(--white);
    border-radius: 34px;
    box-shadow: 3px 6px 12px var(--shadow);
    overflow: hidden;
  }
  .service--tax { left: 167px; }
  .service--accounting { left: 564px; }
  .service__corner {
    position: absolute; left: 0; top: 0;
    width: 112px; height: 96px;
    background: var(--teal);
    border-bottom-right-radius: 100% 100%;
  }
  .service__corner svg { position: absolute; left: 22px; top: 14px; }
  .service__title {
    position: absolute; top: 20px;
    font-size: 26px; font-weight: 700; color: var(--teal);
    padding-bottom: 4px; border-bottom: 2px solid var(--teal);
  }
  .service--tax .service__title { left: 150px; }
  .service--accounting .service__title { left: 120px; }
  .service__text {
    position: absolute; left: 24px; top: 128px; width: 270px;
    font-size: 13.5px; line-height: 1.33; letter-spacing: 0.3px; color: var(--ink);
  }

  .site-url {
    position: absolute; left: 60px; top: 1406px;
    font-size: 17px; font-weight: 500; color: var(--ink);
  }
  .brand-name {
    position: absolute; right: 66px; top: 1330px; width: 150px;
    text-align: right;
    font-size: 26px; font-weight: 500; line-height: 1.1;
    color: var(--teal);
  }
</style>
</head>
<body>
<main class="sheet">
  <section class="values-panel">
    <h1 class="values-heading">CORE <span class="dark">VALUE</span></h1>

    <article class="value value--empower" style="top:60px">
      <div class="value__halo"></div>
      <div class="value__bar">
        <h2 class="value__title">EMPOWER</h2>
        <p class="value__text">we are dedicated, appreciative and respectful of people's time and purpose.</p>
      </div>
      <div class="value__icon">
        <svg width="54" height="54" viewBox="0 0 54 54" fill="var(--teal)">
          <circle cx="27" cy="12" r="7"/>
          <path d="M18 30a9 9 0 0 1 18 0z"/>
          <path d="M4 22l6 14 10 8v6h-5v-4l-10-9-3-14z"/>
          <path d="M50 22l-6 14-10 8v6h5v-4l10-9 3-14z"/>
        </svg>
      </div>
    </article>

    <article class="value value--client" style="top:251px">
      <div class="value__halo"></div>
      <div class="value__bar">
        <h2 class="value__title">CLIENT FOCUSED</h2>
        <p class="value__text">we provide a personal service that goes above the standards of professional care.</p>
      </div>
      <div class="value__icon">
        <svg width="54" height="54" viewBox="0 0 54 54" fill="none" stroke="var(--yellow)" stroke-width="2.5">
          <circle cx="27" cy="24" r="16"/>
          <circle cx="27" cy="24" r="9"/>
          <path d="M27 3v8M27 37v8M6 24h8M40 24h8M6 50h42"/>
        </svg>
      </div>
    </article>

    <article class="value value--rectitude" style="top:442px">
      <div class="value__halo"></div>
      <div class="value__bar">
        <h2 class="value__title">RECTITUDE</h2>
        <p class="value__text">we know the difference between what we have the right to do and what the right thing to do is.</p>
      </div>
      <div class="value__icon">
        <svg width="54" height="54" viewBox="0 0 54 54" fill="var(--charcoal)">
          <rect x="25" y="8" width="4" height="38"/>
          <rect x="8" y="12" width="38" height="4"/>
          <rect x="18" y="46" width="18" height="5"/>
          <path d="M3 30h16l-8-14zM35 30h16l-8-14z"/>
        </svg>
      </div>
    </article>

    <article class="value value--relentless" style="top:633px">
      <div class="value__halo"></div>
      <div class="value__bar">
        <h2 class="value__title">RELENTLESS</h2>
        <p class="value__text">we believe that the longer we try to do our best, the better we become.</p>
      </div>
      <div class="value__icon">
        <svg width="54" height="54" viewBox="0 0 54 54">
          <path d="M6 8h42v30H32l-5 8-5-8H6z" fill="var(--crimson)"/>
          <rect x="24.5" y="13" width="5" height="12" rx="2.5" fill="var(--white)"/>
          <circle cx="27" cy="31" r="3" fill="var(--white)"/>
        </svg>
      </div>
    </article>
  </section>

  <h2 class="brand-promise"><span class="accent">BRAND PROMISE – </span>TRUST, TRANSPARENCY AND DEPENDABILITY</h2>

  <article class="service service--tax">
    <div class="service__corner">
      <svg width="46" height="50" viewBox="0 0 46 50" fill="var(--white)">
        <rect x="2" y="2" width="32" height="42" rx="2"/>
        <text x="6" y="14" font-family="Montserrat, sans-serif" font-size="10" font-weight="700" fill="var(--teal)">TAX</text>
        <rect x="6" y="20" width="22" height="2.5" fill="var(--teal)"/>
        <rect x="6" y="26" width="22" height="2.5" fill="var(--teal)"/>
        <rect x="6" y="32" width="14" height="2.5" fill="var(--teal)"/>
        <rect x="37" y="32" width="6" height="12" rx="2"/>
      </svg>
    </div>
    <h3 class="service__title">Tax</h3>
    <p class="service__text">Maple Finch provides all clients with a trusted tax advisor who provides accuracy in all filings and ensures your compliance with all government agencies.</p>
  </article>

  <article class="service service--accounting">
    <div class="service__corner">
      <svg width="50" height="50" viewBox="0 0 50 50" fill="var(--white)">
        <circle cx="11" cy="14" r="9"/>
        <rect x="3" y="28" width="14" height="3"/>
        <rect x="3" y="34" width="14" height="3"/>
        <rect x="3" y="40" width="10" height="3"/>
        <rect x="24" y="2" width="22" height="34" rx="3"/>
        <rect x="27" y="6" width="16" height="7" fill="var(--teal)"/>
        <rect x="30" y="36" width="12" height="12" rx="3"/>
      </svg>
    </div>
    <h3 class="service__title">Accounting</h3>
    <p class="service__text">Maple Finch provides all business owners with the financial visibility needed to foster growth and facilitate goals.</p>
  </article>

  <p class="site-url">www.maplefinchadvisory.com</p>
  <p class="brand-name">Maple Finch Advisory</p>
</main>
</body>
</html>
```